Real Estate For Sale Yard Sign

18 inches width, height 24 inches
this will hang from a white frame
Seeking a modern, luxury vibe
Needs to have: (must be clear and easy to read if someone is driving by)
For Sale
Cobblestone Summit Homes ( logo)
Delia Harrow Broker/Owner
TK Harrow Realtor/Owner
512-473-6091
QR Code that codes to website (will provide website)

We are a husband and wife team so also would like our picture on the sign

Attached is color palette I like- we want warm, inviting, approachable and a luxury feel even though most of our clients are not luxury we want them to feel valued and treated like they are top tier.

Sign must be easy to read- the example sign is not easy to read. I just submitted it because I like the way the greenery is in background how it’s blended into sign. But the rest of font blends in too much.

Also attached is our logo

Target Market(s)

People selling their home and buyers looking for homes

Industry/Entity Type

Real estate

Requirements
Must have
• Very clear and easy to read

```html
<!DOCTYPE html>
<html lang="en">
<head>
<meta charset="utf-8">
<title>Cobblestone Summit Homes – For Sale Sign</title>
<link href="https://fonts.googleapis.com/css2?family=Playfair+Display:wght@700;800&family=Montserrat:wght@400;500;600;700&display=swap" rel="stylesheet">
<style>
  :root {
    --cream: #f6f1e7;
    --gold: #a88450;
    --gold-light: #b8925a;
    --ink: #0b0b0b;
    --text-dark: #1a1a1a;
    --white: #ffffff;
  }
  html, body {
    margin: 0;
    padding: 0;
    width: 900px;
    height: 1200px;
    overflow: hidden;
    background: var(--white);
  }
  .sign {
    position: relative;
    width: 900px;
    height: 1200px;
    background: var(--cream);
    overflow: hidden;
    font-family: "Montserrat", sans-serif;
  }
  .agent-photo {
    position: absolute;
    left: 400px;
    top: 0;
    width: 500px;
    height: 770px;
    background:
      linear-gradient(90deg, var(--cream) 0%, rgba(246,241,231,0) 22%),
      linear-gradient(165deg, #2e382b 0%, #4f5e45 30%, #b49872 58%, #c8703f 78%, #e7dac8 100%);
  }
  .brand-name {
    position: absolute;
    left: 20px;
    top: 72px;
    width: 460px;
    text-align center;
    text-align: center;
    font-family: "Playfair Display", serif;
    font-weight: 700;
    font-size: 30px;
    line-height: 1.2;
    letter-spacing: 1px;
    color: var(--text-dark);
    text-transform: uppercase;
    white-space: nowrap;
  }
  .headline {
    position: absolute;
    left: 56px;
    margin: 0;
    font-family: "Playfair Display", serif;
    font-weight: 800;
    font-size: 158px;
    line-height: 1;
  }
  .headline-for { top: 176px; color: var(--gold); }
  .headline-sale { top: 312px; color: var(--ink); letter-spacing: -2px; }
  .rule-gold {
    position: absolute;
    height: 3px;
    background: var(--gold);
  }
  .rule-under-sale { left: 60px; top: 476px; width: 390px; }
  .rule-between-agents { left: 160px; top: 590px; width: 190px; height: 2px; }
  .agent-icon {
    position: absolute;
    left: 61px;
    width: 68px;
    height: 68px;
    border-radius: 50%;
    background: var(--gold);
    display: flex;
    align-items: center;
    justify-content: center;
  }
  .agent-icon-key { top: 508px; }
  .agent-icon-home { top: 608px; }
  .agent-name {
    position: absolute;
    left: 160px;
    font-weight: 700;
    font-size: 25px;
    letter-spacing: 3px;
    color: var(--text-dark);
  }
  .agent-role {
    position: absolute;
    left: 160px;
    font-weight: 500;
    font-size: 21px;
    letter-spacing: 2.5px;
    color: var(--gold-light);
  }
  .agent-1-name { top: 510px; }
  .agent-1-role { top: 546px; }
  .agent-2-name { top: 614px; }
  .agent-2-role { top: 650px; }
  .contact-panel {
    position: absolute;
    left: 0;
    top: 0;
    width: 900px;
    height: 1200px;
  }
  .phone-badge {
    position: absolute;
    left: 58px;
    top: 762px;
    width: 106px;
    height: 106px;
    border-radius: 50%;
    background: var(--gold);
    display: flex;
    align-items: center;
    justify-content: center;
  }
  .phone-number {
    position: absolute;
    left: 200px;
    top: 764px;
    font-weight: 600;
    font-size: 84px;
    letter-spacing: 8px;
    color: var(--white);
    line-height: 100px;
    white-space: nowrap;
  }
  .divider-line {
    position: absolute;
    top: 885px;
    height: 2px;
    background: var(--gold);
  }
  .divider-left { left: 58px; width: 380px; }
  .divider-right { left: 462px; width: 382px; }
  .divider-diamond {
    position: absolute;
    left: 443px;
    top: 879px;
    width: 14px;
    height: 14px;
    background: var(--gold);
    transform: rotate(45deg);
  }
  .tagline {
    position: absolute;
    left: 0;
    top: 906px;
    width: 900px;
    text-align: center;
    font-weight: 600;
    font-size: 21px;
    letter-spacing: 3px;
    color: var(--gold-light);
  }
  .qr-slot {
    position: absolute;
    left: 100px;
    top: 957px;
    width: 158px;
    height: 158px;
    background: var(--white);
    border: 4px solid var(--gold);
    border-radius: 14px;
  }
  .qr-separator {
    position: absolute;
    left: 293px;
    top: 970px;
    width: 3px;
    height: 133px;
    background: var(--gold);
  }
  .web-icon {
    position: absolute;
    left: 313px;
    top: 997px;
  }
  .web-address {
    position: absolute;
    left: 404px;
    top: 1010px;
    font-weight: 600;
    font-size: 33px;
    letter-spacing: 0.5px;
    color: var(--white);
    white-space: nowrap;
  }
  .values-band {
    position: absolute;
    left: 0;
    top: 1139px;
    width: 900px;
    height: 61px;
    background: var(--gold);
    display: flex;
    align-items: center;
    justify-content: center;
    font-weight: 500;
    font-size: 24px;
    letter-spacing: 6px;
    color: var(--text-dark);
  }
  .values-band .dot { margin: 0 22px; }
</style>
</head>
<body>
<main class="sign">
  <div class="agent-photo" role="img" aria-label="Photo of the husband and wife agent team, Delia and TK Harrow, standing outdoors among greenery"></div>

  <div class="brand-name">Cobblestone Summit<br>Homes</div>

  <h1 class="headline headline-for">FOR</h1>
  <h1 class="headline headline-sale">SALE</h1>
  <div class="rule-gold rule-under-sale"></div>

  <div class="agent-icon agent-icon-key">
    <svg width="38" height="38" viewBox="0 0 40 40" aria-hidden="true">
      <circle cx="27" cy="13" r="8" fill="none" stroke="#fff" stroke-width="4"/>
      <path d="M21 19 L7 33 M11 29 L15 33 M14 26 L17 29" stroke="#fff" stroke-width="4" stroke-linecap="round" fill="none"/>
    </svg>
  </div>
  <div class="agent-name agent-1-name">DELIA HARROW</div>
  <div class="agent-role agent-1-role">BROKER/ OWNER</div>
  <div class="rule-gold rule-between-agents"></div>

  <div class="agent-icon agent-icon-home">
    <svg width="40" height="40" viewBox="0 0 40 40" aria-hidden="true">
      <path d="M4 20 L20 6 L36 20" stroke="#fff" stroke-width="4" fill="none" stroke-linejoin="round" stroke-linecap="round"/>
      <path d="M9 18 V34 H31 V18" stroke="#fff" stroke-width="4" fill="none" stroke-linejoin="round"/>
      <rect x="16" y="23" width="8" height="11" fill="#fff"/>
    </svg>
  </div>
  <div class="agent-name agent-2-name">TK HARROW</div>
  <div class="agent-role agent-2-role">SALES AGENT / OWNER</div>

  <svg class="contact-panel" width="900" height="1200" viewBox="0 0 900 1200" aria-hidden="true">
    <path d="M0 680 Q450 836 900 680 V1200 H0 Z" fill="#0b0b0b"/>
    <path d="M0 676 Q450 832 900 676" fill="none" stroke="#a88450" stroke-width="9"/>
  </svg>

  <div class="phone-badge">
    <svg width="58" height="58" viewBox="0 0 24 24" aria-hidden="true">
      <path d="M6.6 10.8a15.1 15.1 0 0 0 6.6 6.6l2.2-2.2a1 1 0 0 1 1-.25 11.4 11.4 0 0 0 3.6.57 1 1 0 0 1 1 1V20a1 1 0 0 1-1 1A17 17 0 0 1 3 4a1 1 0 0 1 1-1h3.5a1 1 0 0 1 1 1c0 1.25.2 2.45.57 3.57a1 1 0 0 1-.25 1z" fill="#fff"/>
    </svg>
  </div>
  <div class="phone-number">512-473-6091</div>

  <div class="divider-line divider-left"></div>
  <div class="divider-diamond"></div>
  <div class="divider-line divider-right"></div>

  <div class="tagline">LOCAL EXPERT. PERSONAL SERVICE. PROVEN RESULT.</div>

  <div class="qr-slot" role="img" aria-label="QR code linking to the website"></div>
  <div class="qr-separator"></div>

  <svg class="web-icon" width="66" height="66" viewBox="0 0 66 66" aria-hidden="true">
    <g fill="none" stroke="#a88450" stroke-width="3">
      <circle cx="33" cy="33" r="30"/>
      <ellipse cx="33" cy="33" rx="13" ry="30"/>
      <line x1="33" y1="3" x2="33" y2="63"/>
      <line x1="3" y1="33" x2="63" y2="33"/>
      <path d="M8 18 H58 M8 48 H58"/>
    </g>
  </svg>
  <div class="web-address">CSSUMMITHOMES.COM</div>

  <div class="values-band">
    <span>INTEGRITY</span><span class="dot">•</span><span>EXPERTISE</span><span class="dot">•</span><span>COMMITMENT</span>
  </div>
</main>
</body>
</html>
```